Travel Company Itinerary and Travel Packet

I run a travel company (agency) that organizes trips (any length i.e. day, week, month, or longer) to countries (Israel, Italy, Greece, etc). Regardless of the destination, we want to provide appealing, professional, and clean materials. We are a firm believer that our product is not just the trip but in everything we do...from our communication to our written/printed materials and online presence. Today we are specifically looking for a template that we can use to share one's trip/itinerary. Ideally what you would create would be a template we could populate with specific information for the client about the day-to-day of their trip, who we are, the hotels they are staying in, the highlights, what to pack, and where to eat, etc. To be more specific, this template should consist of the following:
1. Title Page (including contact info...however this could go where you see fit)
2. About Us (blurb about us at the company),
3. A highlights page of the trip and services included - this could be used as standalone marketing material for our clients to promote trips. (look at the Italy example)
4. A timeline of the process
5. A summary of the trip, bullet point/all one 1 page
6. A day-by-day itinerary page of what they are doing, and where they are staying (each day on its own page - should be the same template repeated for each day.
7. Recommended Hotels to choose from
8. Recommended Restaurants to eat at
9. A pricing page (per person, per group, itemized down to each experience.
10. A packing List
11. A letterhead that could be used for a cover letter
12. Each page should use pictures...a template where one could insert photos per page based on where the trip is going as well as stock imaging that brings the document to life for the reader. (see examples in uploaded files).

We've attached a few that we've seen in the industry that appeals to us and our tastes, but the template we are looking for is even more eye-popping, user-friendly, and communicates a high level of service just by seeing the document. It communicates our brand. Each attached example has elements we like and don't like and will give you. a good picture (we hope), but you'll notice the list we gave you provides a more robust end product...in other words we want more than these examples as we see great potential in including each layer of information with the ability to pick and choose what to include (from all of it to just the highlights page).

Link to Brand Assets- https://files.plovanexa.net/share/folders/8Kd24mTqZrw91XbLcVn3pYe60hJ?mode=view
Updates

We need a few days to review the designs and had a few requests for an extension if possible. I've also uploaded sample itineraries for Israel as requested by a few designers. Much appreciated

Target Market(s)

Any client of ours traveling - school, groups, families, big spenders etc

Industry/Entity Type

Travel Industry

Requirements
Must have
• See above list - if clarification is needed, I'm happy to give.

```html
<!DOCTYPE html>
<html lang="en">
<head>
<meta charset="utf-8">
<title>Veranor — Trip Packet</title>
<link rel="stylesheet" href="https://fonts.googleapis.com/css2?family=Montserrat:ital,wght@0,300;0,400;0,600;0,700&family=Open+Sans:ital,wght@0,400;1,400&display=swap">
<style>
  :root {
    --frame: #1a1a1a;
    --paper: #ffffff;
    --navy: #1d3a50;
    --orange: #d98a42;
    --yellow: #e8e07a;
    --teal: #2aa6b8;
    --ink: #3d4852;
    --body: #8b9096;
    --photo-coast: linear-gradient(120deg, #4f8fa0 0%, #8aa1a0 25%, #b39b6e 55%, #a88e63 100%);
    --photo-dune: linear-gradient(160deg, #4d86c4 0%, #8fb3d6 18%, #d1733c 35%, #c9622c 70%, #b4552a 100%);
  }
  * { margin: 0; padding: 0; box-sizing: border-box; }
  html, body { width: 1200px; height: 860px; overflow: hidden; background: var(--frame); }
  .spread {
    position: absolute; left: 12px; top: 12px; width: 1176px; height: 836px;
    background: var(--paper); overflow: hidden;
  }
  .photo { position: absolute; top: 0; height: 223px; }
  .photo-left { left: 0; width: 590px; background: var(--photo-coast); }
  .photo-right { left: 590px; width: 586px; background: var(--photo-dune); }
  .folio {
    position: absolute; top: 54px; font: 400 9px "Montserrat", sans-serif;
    color: rgba(255,255,255,0.85); letter-spacing: 0.5px;
  }
  .folio-left { left: 540px; }
  .folio-right { left: 1119px; }

  .brand {
    position: absolute; left: 36px; top: 288px; display: flex; align-items: center; gap: 10px;
  }
  .brand-dot { width: 22px; height: 22px; border-radius: 50%; background: var(--orange); }
  .brand-name { font: 600 34px "Montserrat", sans-serif; color: var(--navy); letter-spacing: 0.5px; }
  .divider { position: absolute; left: 237px; top: 263px; width: 2px; height: 80px; background: var(--orange); }
  .section-title { position: absolute; left: 252px; top: 272px; color: var(--ink); font-family: "Montserrat", sans-serif; }
  .section-title .small { display: block; font-weight: 400; font-size: 29px; line-height: 28px; }
  .section-title .large { display: block; font-weight: 300; font-size: 41px; line-height: 44px; }

  .story { position: absolute; left: 37px; top: 372px; width: 532px; }
  .story p {
    font: 400 11.1px/17.5px "Montserrat", sans-serif; color: var(--body);
    margin-bottom: 17.5px;
  }
  .story p.spaced { margin-top: 17.5px; }

  .feature-title { position: absolute; left: 633px; top: 270px; color: var(--ink); font-family: "Montserrat", sans-serif; }
  .feature-title .small { display: block; font-weight: 600; font-size: 21px; line-height: 22px; }
  .feature-title .large { display: block; font-weight: 300; font-size: 38px; line-height: 40px; }

  .columns { position: absolute; left: 635px; top: 346px; display: flex; gap: 19px; }
  .columns p {
    width: 150px; font: 400 8.9px/15.6px "Open Sans", sans-serif; color: var(--body);
    text-align: justify; hyphens: auto;
  }

  .counter { position: absolute; top: 614px; width: 255px; }
  .counter-one { left: 633px; }
  .counter-two { left: 896px; }
  .counter h3 { font: 400 17px/20px "Montserrat", sans-serif; color: var(--ink); margin-bottom: 10px; }
  .counter ul { list-style: none; }
  .counter li {
    display: flex; align-items: center; gap: 11px; height: 25.3px;
    font: italic 400 9.2px "Open Sans", sans-serif; color: var(--body); white-space: nowrap;
  }
  .counter svg { flex: none; }

  .footer { position: absolute; left: 0; top: 810px; width: 1176px; height: 26px; }
  .footer svg { position: absolute; inset: 0; }
  .footer span { position: absolute; top: 5px; font: 400 12.5px "Montserrat", sans-serif; color: #fff; }
  .footer .page-left { left: 36px; }
  .footer .url-left { left: 451px; }
  .footer .url-right { left: 612px; }
  .footer .page-right { left: 1091px; }
</style>
</head>
<body>
<main class="spread">
  <div class="photo photo-left" role="img" aria-label="Tandem paragliding pair flying above a sandy coastal cliff and the sea"></div>
  <div class="photo photo-right" role="img" aria-label="Sandboarder riding down a red desert dune under a blue sky"></div>
  <span class="folio folio-left">11</span>
  <span class="folio folio-right">12</span>

  <div class="brand"><span class="brand-dot"></span><span class="brand-name">Veranor</span></div>
  <div class="divider"></div>
  <h1 class="section-title"><span class="small">Our</span><span class="large">Statistics</span></h1>

  <section class="story">
    <p>Every journey we plan begins with a conversation about who is travelling, what moves them and how they like to explore. Since our first group tour we have guided schools, families, congregations and private travellers through Israel, Italy, Greece and beyond, handling flights, hotels, guides and transfers so our guests can focus on the moments that matter. Each itinerary in this packet is built day by day, with the hotels you will stay in, the highlights you will see, the restaurants we recommend and a clear picture of what is included in your price.</p>
    <p>Over the years our team has welcomed thousands of travellers on trips lasting a single day, a week, a month or longer. We work with licensed local guides, trusted drivers and hand-picked hotels in every region we visit, and a member of our staff is reachable around the clock while you are on the road. The pages that follow explain the process from booking to return.</p>
    <p class="spaced">Use the summary, daily pages, pricing table and packing list together or on their own, and bring this packet with you. Questions before departure? Our planners are happy to walk you through every detail of your trip.</p>
  </section>

  <h2 class="feature-title"><span class="small">Day 01 · Arrival</span><span class="large">Coast &amp; Dunes</span></h2>

  <section class="columns">
    <p>Morning: your guide meets the group at arrivals with a welcome sign and bottled water. A private coach takes everyone along the coastal road to the hotel, where luggage is stored while rooms are prepared. After a short orientation walk along the promenade, enjoy a relaxed brunch overlooking the sea and time to rest, change money or simply settle in before the afternoon begins.</p>
    <p>Afternoon: we head south to the cliffs for an optional tandem paraglide with certified pilots, or a gentle walk along the ridge trail for those who prefer to stay grounded. Later the coach continues to the red dunes, where instructors run a short sandboarding lesson. Sunscreen, closed shoes and a light layer are recommended, and cold drinks are provided.</p>
    <p>Evening: return to the Harbor Stone Hotel, a four-star seafront property with a pool, rooftop terrace and breakfast included each morning. Dinner is served at Olive &amp; Salt, a short walk from the lobby, with vegetarian and kosher menus available on request. Overnight at the hotel, with a wake-up call set for the next day of the trip.</p>
  </section>

  <section class="counter counter-one">
    <h3>Included Services</h3>
    <ul>
      <li><svg width="13" height="12" viewBox="0 0 13 12"><path d="M1 6.5 L4.8 10.5 L12 1" fill="none" stroke="var(--teal)" stroke-width="2.6" stroke-linecap="round" stroke-linejoin="round"/></svg>Airport meet and greet with private transfer</li>
      <li><svg width="13" height="12" viewBox="0 0 13 12"><path d="M1 6.5 L4.8 10.5 L12 1" fill="none" stroke="var(--teal)" stroke-width="2.6" stroke-linecap="round" stroke-linejoin="round"/></svg>Licensed local guide for every touring day</li>
      <li><svg width="13" height="12" viewBox="0 0 13 12"><path d="M1 6.5 L4.8 10.5 L12 1" fill="none" stroke="var(--teal)" stroke-width="2.6" stroke-linecap="round" stroke-linejoin="round"/></svg>Four-star hotels with daily breakfast</li>
      <li><svg width="13" height="12" viewBox="0 0 13 12"><path d="M1 6.5 L4.8 10.5 L12 1" fill="none" stroke="var(--teal)" stroke-width="2.6" stroke-linecap="round" stroke-linejoin="round"/></svg>Entrance fees to all listed sites and parks</li>
      <li><svg width="13" height="12" viewBox="0 0 13 12"><path d="M1 6.5 L4.8 10.5 L12 1" fill="none" stroke="var(--teal)" stroke-width="2.6" stroke-linecap="round" stroke-linejoin="round"/></svg>Sandboarding lesson and equipment hire</li>
      <li><svg width="13" height="12" viewBox="0 0 13 12"><path d="M1 6.5 L4.8 10.5 L12 1" fill="none" stroke="var(--teal)" stroke-width="2.6" stroke-linecap="round" stroke-linejoin="round"/></svg>24-hour support line throughout your trip</li>
    </ul>
  </section>

  <section class="counter counter-two">
    <h3>Packing List</h3>
    <ul>
      <li><svg width="13" height="12" viewBox="0 0 13 12"><path d="M1 6.5 L4.8 10.5 L12 1" fill="none" stroke="var(--teal)" stroke-width="2.6" stroke-linecap="round" stroke-linejoin="round"/></svg>Passport valid six months beyond your return</li>
      <li><svg width="13" height="12" viewBox="0 0 13 12"><path d="M1 6.5 L4.8 10.5 L12 1" fill="none" stroke="var(--teal)" stroke-width="2.6" stroke-linecap="round" stroke-linejoin="round"/></svg>Comfortable walking shoes and closed sandals</li>
      <li><svg width="13" height="12" viewBox="0 0 13 12"><path d="M1 6.5 L4.8 10.5 L12 1" fill="none" stroke="var(--teal)" stroke-width="2.6" stroke-linecap="round" stroke-linejoin="round"/></svg>Sun hat, sunglasses and high-factor sunscreen</li>
      <li><svg width="13" height="12" viewBox="0 0 13 12"><path d="M1 6.5 L4.8 10.5 L12 1" fill="none" stroke="var(--teal)" stroke-width="2.6" stroke-linecap="round" stroke-linejoin="round"/></svg>Modest layer covering shoulders and knees</li>
      <li><svg width="13" height="12" viewBox="0 0 13 12"><path d="M1 6.5 L4.8 10.5 L12 1" fill="none" stroke="var(--teal)" stroke-width="2.6" stroke-linecap="round" stroke-linejoin="round"/></svg>Refillable water bottle and small day pack</li>
      <li><svg width="13" height="12" viewBox="0 0 13 12"><path d="M1 6.5 L4.8 10.5 L12 1" fill="none" stroke="var(--teal)" stroke-width="2.6" stroke-linecap="round" stroke-linejoin="round"/></svg>Universal plug adapter and phone charger</li>
    </ul>
  </section>

  <footer class="footer">
    <svg width="1176" height="26" viewBox="0 0 1176 26">
      <polygon points="0,0 1176,0 1176,26 0,26" fill="var(--navy)"/>
      <polygon points="0,0 165,0 185,26 0,26" fill="var(--orange)"/>
      <polygon points="165,0 181,0 207,26 185,26" fill="var(--yellow)"/>
      <polygon points="1000,0 1016,0 996,26 980,26" fill="var(--yellow)"/>
      <polygon points="1016,0 1176,0 1176,26 996,26" fill="var(--orange)"/>
    </svg>
    <span class="page-left">Page: 01</span>
    <span class="url-left">www.goveranor.com</span>
    <span class="url-right">www.goveranor.com</span>
    <span class="page-right">Page: 01</span>
  </footer>
</main>
</body>
</html>
```